Modern Website Design for an Online Travel Agency.. Design Only!!

Hi there!

We are building an website for our travel agency that caters to tourists traveling to the Cayman Islands. We provide travel information and take bookings for various tours available here.

We need designs for 8 different web page layouts. You can see the layout specifications in two attached documents. We do not have a need for the coding to be done. This will simply act as a blueprint for our developer to build from.

The important pages are the 'Home Page' 'checkout page' and the ‘Checkout Page’ (Page 1 & 10 in the PDF ‘Website Layout’)

The MOST important page is ‘Tour Search Page’ (page 6)

If you intend on only submitting one page design, please submit a design for page 6. Be aware though, the more of these 3 page designs you submit, the more likely we are to move forward with you!

At this stage, we are simply looking to develop the most aesthetic website design layout possible.

- The website should be colour coordinated with the logo. You can most certainly use other colours if you feel they complement the overall design of the website well.

- Everything must be laid out in an EXTREMELY simple & ‘easy to navigate’ way. The key is simplicity & Functionality. There is no need for messy or elaborate graphics.

- The website MUST have a VERY clean and modern appearance.

- We want the main background to be white, but you can use light grey in places to compliment or add dimension if you feel necessary.

- We will appreciate a good use of shadows and especially a good use of icons. (You can see examples of icons we have already designed, we are definitely open to new icon design concepts too)

- We will reward imagination and original thinking! Essentially we want a website with a creative touch and unique design elements, whilst maintaining that clean and simple layout.

- Most importantly!! - Paying attention to the small details will be highly rewarded (A well balanced and seamless use of fonts, colours, dimensions, shadowing, positioning, etc)

If you have any questions, please don’t hesitate to ask.

We’re excited to see your design submissions!

Thank you!!

You can find all the support documents and content at: https://www.filevorra.net/sh/9qm2rtwplexan7c/QQBmTtZnPdLsWEGxvvaJpLmRw?dl=0

Target Market(s)

Tourists

Industry/Entity Type

Travel

Number of Pages Required

5+ page

Font styles to use
Sans Serif

Colors

Designer to choose colors to be used in the design.

Requirements
Must have
• Must be very clean and modern.
• Must be simple and bold
• Must be color coordinated in a way that makes sense
• White background
Nice to have
• Good use of shadows and Icons
Should not have
• Over use of messy graphics
• And design layout which is not right angled (using anything but vertical or horizontal for the edges in the design)

```html
<!DOCTYPE html>
<html lang="en">
<head>
<meta charset="utf-8">
<title>Coral Shoal – IsleRoute</title>
<link rel="stylesheet" href="https://fonts.googleapis.com/css2?family=Poppins:wght@400;500;600;700&family=Lato:wght@400;700&display=swap">
<style>
:root{
  --blue:#0b63d1;
  --blue-dark:#0a4fa8;
  --green:#6cb024;
  --navy:#0f1e2c;
  --text:#1d1d1d;
  --muted:#7d7d7d;
  --line:#e3e3e3;
  --grey-bg:#f1f1f1;
  --green-bg:#e3f0d6;
  --red-bg:#f9cdcd;
  --blue-bg:#d5e5f6;
  --red:#d42020;
  --light:#eaf1fa;
}
*{box-sizing:border-box;margin:0;padding:0}
html,body{width:1200px;height:4535px;overflow:hidden}
body{position:relative;background:#fff;font-family:"Lato",sans-serif;color:var(--text);font-size:13px}
.abs{position:absolute}
h1,h2,h3,.poppins{font-family:"Poppins",sans-serif}
.btn{position:absolute;display:flex;align-items:center;justify-content:center;font-family:"Poppins",sans-serif;font-weight:600;font-size:14px;color:#fff;background:var(--blue)}
.btn-outline{background:#fff;color:var(--blue);border:1.5px solid var(--blue)}

/* header */
.site-header{position:absolute;left:0;top:0;width:1200px;height:63px;background:#fff}
.brand{position:absolute;left:170px;top:17px;display:flex;align-items:center;gap:8px;font-family:"Poppins",sans-serif;font-weight:600;font-size:22px;color:var(--green)}
.brand i{width:22px;height:22px;background:var(--blue);display:block}
.nav{position:absolute;left:0;top:23px;font-family:"Poppins",sans-serif;font-size:11.5px;color:#222}
.nav span{position:absolute;top:0;white-space:nowrap}
.nav-right{position:absolute;left:885px;top:21px;display:flex;gap:22px;font-family:"Poppins",sans-serif;font-weight:600;font-size:13px;color:var(--blue)}

/* hero */
.hero{position:absolute;left:0;top:63px;width:1200px;height:592px;background:linear-gradient(180deg,#2f7fe6 0%,#5fa4ef 35%,#6b9e4a 55%,#3e7b7a 72%,#2a79b8 82%,#e6dcc6 100%)}
.hero-panel{position:absolute;left:0;top:137px;width:591px;height:316px;background:rgba(18,36,54,.92)}
.hero-title{position:absolute;left:170px;top:170px;font-size:56px;font-weight:700;color:var(--green);line-height:1;white-space:nowrap}
.hero-text{position:absolute;left:170px;top:254px;width:400px;color:#fff;font-size:15px;line-height:24px}
.hero-btn{left:170px;top:354px;width:180px;height:51px;font-weight:500;font-size:16px;gap:10px}

/* details */
.crumb{left:170px;top:682px;font-family:"Poppins",sans-serif;font-weight:600;font-size:15px}
.tabs{position:absolute;left:170px;top:744px;width:553px;height:32px;border-bottom:1px solid var(--line);display:flex;gap:30px;font-family:"Poppins",sans-serif;font-size:12px}
.tabs span{padding-bottom:10px}
.tabs .on{color:var(--blue);font-weight:600;border-bottom:2px solid var(--blue)}
.act-title{left:170px;top:810px;font-family:"Poppins",sans-serif;font-size:28px;display:flex;align-items:baseline;gap:20px;white-space:nowrap}
.act-title b{color:var(--green);font-weight:600;font-size:28px}
.act-title small{font-size:11px;color:var(--muted);font-weight:400}
.lead{left:170px;top:872px;width:550px;font-family:"Poppins",sans-serif;font-size:13.5px;line-height:20px}
.para{left:170px;width:550px;font-size:11.5px;line-height:20px;color:var(--muted)}
.facts{left:170px;top:1112px;width:553px;display:flex}
.fact{flex:1;padding-right:10px;border-right:1px solid var(--line);padding-left:0}
.fact+.fact{padding-left:18px}
.fact:last-child{border:none}
.fact h4{font-family:"Poppins",sans-serif;font-weight:600;font-size:12px;margin:10px 0 10px}
.fact p{font-size:11.5px;color:var(--muted)}
.organizer{left:170px;top:1225px;width:552px;height:63px;background:#e4e4e4;display:flex;align-items:center;justify-content:center;gap:12px;font-size:11.5px;color:var(--muted)}
.organizer i{width:46px;height:46px;border-radius:50%;background:#5a2a1e;display:block}
.organizer a{color:var(--blue);text-decoration:underline}

.photos-btn{left:790px;top:683px;width:181px;height:51px;gap:14px;font-size:17px;font-weight:500}
.price-card{position:absolute;left:794px;top:757px;width:301px;height:514px;background:#fff;box-shadow:0 3px 14px rgba(0,0,0,.12)}
.price-top{position:absolute;left:0;top:0;width:301px;height:100px;color:#fff;text-align:center}
.price-top svg{position:absolute;left:0;top:0}
.price-top .from{position:relative;padding-top:14px;font-family:"Poppins",sans-serif;font-size:12px;font-weight:600}
.price-top .amt{position:relative;font-family:"Poppins",sans-serif;font-size:32px;font-weight:600;margin-top:2px}
.price-top .amt small{font-size:12px;font-weight:400}
.stars{position:absolute;top:118px;width:100%;text-align:center;color:#f4b400;font-size:26px;letter-spacing:4px}
.reviews{position:absolute;top:150px;width:100%;text-align:center;font-family:"Poppins",sans-serif;font-size:13px;font-weight:600;color:#555;text-decoration:underline}
.popular{position:absolute;top:307px;width:100%;text-align:center;font-family:"Poppins",sans-serif;font-weight:600;font-size:12px}
.popular-sub{position:absolute;top:327px;width:100%;text-align:center;font-size:11px;color:#aaa}
.help{position:absolute;top:393px;width:100%;text-align:center;font-family:"Poppins",sans-serif;font-weight:600;font-size:12px}

.rule{left:0;top:1332px;width:1200px;height:1px;background:var(--line)}
.section-title{position:absolute;left:0;width:1200px;text-align:center;font-weight:700;font-size:56px}

/* offer card */
.card{position:absolute;left:169px;width:926px;background:#fff;box-shadow:0 2px 12px rgba(0,0,0,.13)}
.card h3{position:absolute;left:26px;top:48px;font-size:27px;font-weight:600;white-space:nowrap}
.card .price{position:absolute;left:500px;top:58px;font-family:"Poppins",sans-serif;font-weight:600;color:var(--green);font-size:19px;white-space:nowrap}
.card .price small{color:var(--muted);font-size:11px;font-weight:400}
.card .b1{left:684px;top:53px;width:90px;height:38px;font-size:13px}
.card .b2{left:789px;top:53px;width:120px;height:38px;font-size:12px}
.plus{position:absolute;left:441px;width:40px;height:40px;border-radius:50%;background:var(--blue);color:#fff;display:flex;align-items:center;justify-content:center}
.side{position:absolute;left:26px;width:315px;padding:36px 26px 0 26px}
.side h5{font-family:"Poppins",sans-serif;font-weight:600;font-size:19px;margin-bottom:10px}
.side li{list-style:none;font-size:14px;padding-left:32px;line-height:28px}
.side-grey{top:116px;height:238px;background:var(--grey-bg)}
.side-grey li{padding-left:0;color:#444;font-size:14px;line-height:36px;display:flex;align-items:center;gap:12px}
.side-grey li i{width:18px;height:18px;border:2px solid #555;border-radius:50%;display:block}
.side-green{top:354px;height:261px;background:var(--green-bg);padding-top:18px}
.side-green h5,.side-green li{color:var(--green)}
.side-red{top:615px;height:96px;background:var(--red-bg);padding-top:18px}
.side-red h5,.side-red li{color:var(--red)}
.side-blue{top:711px;height:259px;background:var(--blue-bg);padding-top:18px}
.side-blue h5,.side-blue li{color:var(--blue)}
.itin{position:absolute;left:377px;top:116px;width:520px;font-size:11.5px;line-height:20px;color:var(--muted)}
.itin h6{font-family:"Poppins",sans-serif;font-weight:600;font-size:15px;color:var(--text);margin:0 0 14px}
.itin p{margin-bottom:18px}
.itin .strong{color:#333;font-weight:700}

/* map */
.map{position:absolute;left:169px;top:3010px;width:925px;height:346px;background:radial-gradient(ellipse at 70% 50%,#4d6a4c 0%,#3a4a45 40%,#2c3a3f 100%)}
.addr{position:absolute;left:348px;top:163px;width:229px;height:115px;background:#fff;padding:18px 0 0 60px}
.addr h6{font-family:"Poppins",sans-serif;color:var(--blue);font-size:14px;font-weight:600}
.addr p{font-size:11px;color:#555;line-height:20px;margin-top:6px}
.addr svg{position:absolute;left:12px;top:42px}
.addr .btn{left:53px;top:95px;width:124px;height:34px;font-size:13px}

.shot{position:absolute;top:3534px;width:292px;height:197px}
.arrow{position:absolute;top:3614px;width:38px;height:38px;border-radius:50%;background:var(--blue);color:#fff;display:flex;align-items:center;justify-content:center}

/* planner */
.planner{position:absolute;left:0;top:3814px;width:1200px;height:357px;background:var(--light)}
.planner h4{position:absolute;left:172px;top:84px;font-family:"Poppins",sans-serif;font-weight:600;font-size:15px}
.planner p{position:absolute;left:172px;top:120px;width:440px;font-size:11.5px;line-height:20px;color:#666}
.dots{position:absolute;left:82px;top:124px;display:flex;flex-direction:column;gap:18px}
.dots i{width:14px;height:14px;border:1.5px solid var(--blue);border-radius:50%;display:block}
.dots i.on{background:radial-gradient(var(--blue) 40%,transparent 45%)}
.planner .b1{left:170px;top:248px;width:136px;height:36px;font-size:13px}
.planner .b2{left:329px;top:248px;width:102px;height:36px;font-size:13px}
.illus{position:absolute;left:688px;top:20px;width:296px;height:298px;border-radius:50% 0 50% 50%;border:1.5px solid var(--blue);background:radial-gradient(circle at 50% 45%,#dff0c9 0%,#cfe3f6 45%,#fff 75%)}
.illus .play{position:absolute;left:126px;top:244px;width:40px;height:40px;border-radius:50%;background:var(--blue)}

/* footer */
.footer{position:absolute;left:0;top:4171px;width:1200px;height:314px;background:var(--navy);color:#cfd6dd}
.footer .brand{top:44px;left:172px}
.footer h5{position:absolute;top:52px;font-family:"Poppins",sans-serif;color:var(--green);font-weight:600;font-size:16px}
.footer .about{position:absolute;left:172px;top:110px;width:210px;font-size:12px;line-height:20px}
.footer ul{position:absolute;top:110px;list-style:none;font-size:12px;line-height:20px}
.footer ul li::before{content:"";display:inline-block;width:6px;height:6px;border-radius:50%;background:var(--blue);margin-right:12px;vertical-align:middle}
.social{position:absolute;left:172px;top:244px;display:flex;gap:17px}
.social i{width:33px;height:33px;border:1.5px solid var(--blue);border-radius:50%;display:block}
.social i.fill{background:var(--blue)}
.contact{position:absolute;left:880px;top:110px;font-size:12px;line-height:20px}
.contact div{display:flex;gap:22px;margin-bottom:22px;align-items:flex-start}
.copy{position:absolute;left:0;top:4485px;width:1200px;height:50px;background:var(--blue);color:#fff;font-size:12px;display:flex;align-items:center;justify-content:center}
</style>
</head>
<body>

<header class="site-header">
  <div class="brand"><i></i>IsleRoute</div>
  <nav class="nav"><span style="left:408px">Discover Cayman</span><span style="left:536px">Thing to do</span><span style="left:624px">My Trip Planner</span><span style="left:741px">Map</span><span style="left:793px">Contact Us</span></nav>
  <div class="nav-right"><span>USD$</span><span>Login</span></div>
  <a class="btn" style="left:991px;top:16px;width:102px;height:31px;font-size:13px">Destinations</a>
</header>

<section class="hero" role="img" aria-label="Photo of a sunny beach with turquoise sea, trees and swimmers">
  <div class="hero-panel"></div>
  <h1 class="hero-title">Coral Shoal</h1>
  <p class="hero-text">Lorem Ipsum is simply dummy text of the printing and typesetting industry. Lorem Ipsum has been the industry's standard dummy text ever since the 1500s</p>
  <a class="btn hero-btn"><svg width="22" height="24" viewBox="0 0 22 24" fill="none" stroke="#fff" stroke-width="1.8"><path d="M11 22s7-7 7-12a7 7 0 0 0-14 0c0 5 7 12 7 12z"/><circle cx="11" cy="10" r="2.6"/></svg>Cayman Island</a>
</section>

<main>
  <div class="crumb abs">Home / Cayman Island / Coral Shoal</div>
  <div class="tabs"><span class="on">Activity description</span><span>Gallery</span><span>Meeating</span><span>Reviews</span><span>Locations</span></div>
  <h2 class="act-title abs"><span style="font-weight:400">Coral Shoal</span><span><b>$ 9,650</b> <small>/ Per Person</small></span></h2>
  <p class="lead abs">Lorem Ipsum is simply dummy text of the printing and typesetting industry. Lorem Ipsum has been the industry's standard dummy text.</p>
  <p class="para abs" style="top:926px">Lorem Ipsum is simply dummy text of the printing and typesetting industry. Lorem Ipsum has been the industry's standard dummy text ever since the 1500s, when an unknown printer took a galley of type and scrambled it to make a type specimen book.</p>
  <p class="para abs" style="top:1008px">It has survived not only five centuries, but also the leap into electronic typesetting, remaining essentially unchanged. It was popularised in the 1960s with the release of Typemark sheets containing Lorem Ipsum passages, and more recently with desktop publishing software like Pagewright Studio including versions of Lorem Ipsum.</p>

  <div class="facts abs">
    <div class="fact">
      <svg width="32" height="30" viewBox="0 0 32 30" fill="none" stroke-width="3" stroke-linecap="round"><rect x="2" y="6" width="22" height="22" rx="3" stroke="var(--blue)" stroke-width="2"/><path d="M7 16l6 6L29 3" stroke="var(--green)"/></svg>
      <h4>Open Seasons</h4><p>WINTER, SUMMER</p>
    </div>
    <div class="fact">
      <svg width="34" height="30" viewBox="0 0 34 30" fill="none" stroke="var(--blue)" stroke-width="2"><rect x="2" y="2" width="20" height="14" rx="2"/><rect x="12" y="12" width="20" height="14" rx="2" stroke="var(--green)"/><path d="M16 19h12M16 23h8" stroke="var(--green)"/></svg>
      <h4>Languages Spoken</h4><p>English, German</p>
    </div>
    <div class="fact">
      <svg width="30" height="30" viewBox="0 0 30 30" fill="none" stroke="var(--blue)" stroke-width="2"><circle cx="15" cy="15" r="13"/><path d="M15 13v9" stroke="var(--green)" stroke-width="2.6"/><circle cx="15" cy="8.5" r="1.4" fill="var(--green)" stroke="none"/></svg>
      <h4>Cancellation Policy</h4><p>Lorem Ipsum is simply dummy.</p>
    </div>
  </div>
  <div class="organizer abs"><i></i>Organized by <a>reefline</a></div>

  <a class="btn photos-btn"><svg width="32" height="26" viewBox="0 0 32 26" fill="none" stroke="#fff" stroke-width="2"><rect x="1" y="1" width="30" height="24" rx="2"/><path d="M4 21l8-9 6 6 4-4 6 7" stroke="var(--green)"/><circle cx="22" cy="8" r="2.5"/></svg>View Photos</a>

  <aside class="price-card">
    <div class="price-top">
      <svg width="301" height="100" viewBox="0 0 301 100"><path d="M0 0H301V80Q150 108 0 80Z" fill="var(--green)"/></svg>
      <div class="from">FROM</div>
      <div class="amt"><small>$</small>9,650 <small>/ PERSON</small></div>
    </div>
    <div class="stars">★★★★★</div>
    <div class="reviews">30 reviews</div>
    <a class="btn" style="left:31px;top:183px;width:237px;height:46px;font-size:15px">Book Now</a>
    <a class="btn btn-outline" style="left:31px;top:237px;width:237px;height:46px;font-size:13px;gap:8px"><svg width="22" height="22" viewBox="0 0 22 22"><rect x="2" y="8" width="18" height="12" fill="var(--green)"/><rect x="1" y="5" width="20" height="5" fill="var(--blue)"/><rect x="9.5" y="5" width="3" height="15" fill="#fff"/></svg><span style="color:var(--green)">Get Gift</span></a>
    <div class="popular">This offer is very popular</div>
    <div class="popular-sub">1050 people recently chose this activity</div>
    <div class="help">Need Any Help?</div>
    <a class="btn" style="left:20px;top:436px;width:96px;height:40px;font-size:13px">Emial Us</a>
    <a class="btn" style="left:182px;top:436px;width:96px;height:40px;font-size:13px">Call Us</a>
  </aside>

  <div class="rule abs"></div>
  <h2 class="section-title" style="top:1390px">Offers</h2>

  <article class="card" style="top:1515px;height:1028px">
    <h3>1. Coral Shoal</h3>
    <div class="price">$ 9,650 <small>/ Per Person</small></div>
    <a class="btn b1">Book Now</a>
    <a class="btn btn-outline b2">Add to Itinerary</a>

    <ul class="side side-grey">
      <li><i></i>Duration</li><li><i></i>Tour Description</li><li><i></i>Minimum Age</li><li><i></i>Starting Times</li><li><i></i>Meeting Point</li>
    </ul>
    <div class="side side-green"><h5>Included</h5><ul>
      <li>Buffet breakfast at launch site</li><li>Light lunch</li><li>Snacks</li><li>Refreshments</li><li>Wetsuits and diving equipment</li><li>Afternoon tea</li><li>Certificate of attendance</li></ul></div>
    <div class="side side-red"><h5>Excluded</h5><ul><li>Video (350Rand)</li></ul></div>
    <div class="side side-blue"><h5>What to Bring</h5><ul>
      <li>Sunscreen</li><li>Passport or Driving licence</li><li>Swimwear</li><li>Towel</li><li>Camera</li><li>Hat or cap</li><li>A warm jacket</li></ul></div>

    <div class="itin">
      <h6>Itinerary</h6>
      <p>- Lorem Ipsum is simply dummy text of the printing and typesetting industry. Lorem Ipsum has been the industry's standard dummy text ever since the 1500s, when an unknown printer took a galley of type and scrambled it to make a type specimen book.</p>
      <p>- Lorem Ipsum is simply dummy text of the printing and typesetting industry. Lorem Ipsum has been the industry's standard dummy text ever since the 1500s</p>
      <p>- Lorem Ipsum is simply dummy text of the printing and typesetting industry. Lorem Ipsum has been the industry's standard dummy text ever since the 1500s</p>
      <p>- Lorem Ipsum is simply dummy text of the printing and typesetting industry. Lorem Ipsum has been the industry's standard dummy text ever since the 1500s, when an unknown printer took a galley of type and scrambled it to make a type specimen book.</p>
      <p>- Lorem Ipsum is simply dummy text of the printing and typesetting industry. Lorem Ipsum has been the industry's standard dummy text ever since the 1500s</p>
      <p>- Lorem Ipsum is simply dummy text of the printing and typesetting industry. Lorem Ipsum has been the industry's standard dummy text ever since the 1500s</p>
      <p>- Lorem Ipsum is simply dummy text of the printing and typesetting industry. Lorem Ipsum has been the industry's standard dummy text ever since the 1500s, when an unknown printer took a galley of type and scrambled it to make a type specimen book.</p>
      <h6 style="margin-top:34px">Activity requirements</h6>
      <p>Lorem Ipsum is simply dummy text of the printing and typesetting industry. Lorem Ipsum has been the industry's standard dummy text ever since the 1500s</p>
      <h6 style="margin-top:30px">Special terms</h6>
      <p class="strong">- Lorem Ipsum is simply dummy text of the printing and typesetting industry. Lorem Ipsum has been the industry's standard dummy text ever since the 1500s</p>
      <p>- Lorem Ipsum is simply dummy text of the printing and typesetting industry. Lorem Ipsum has been the industry's standard dummy text ever since the 1500s</p>
    </div>
    <div class="plus" style="top:1008px">
      <svg width="16" height="4" viewBox="0 0 16 4"><rect width="16" height="3" fill="#fff"/></svg>
    </div>
  </article>

  <article class="card" style="top:2622px;height:159px">
    <h3 style="top:36px">2. Horse Riding</h3>
    <div class="price" style="top:46px">$ 8,650 <small>/ Per Person</small></div>
    <a class="btn b1" style="top:40px">Book Now</a>
    <a class="btn btn-outline b2" style="top:40px">Add to Itinerary</a>
    <p style="position:absolute;left:26px;top:90px;width:720px;font-size:11.5px;line-height:20px;color:var(--muted)">- Lorem Ipsum is simply dummy text of the printing and typesetting industry. Lorem Ipsum has been the industry's standard dummy text ever since the 1500s, when an unknown printer took a galley of type and scrambled it to make a type specimen book.</p>
    <div class="plus" style="top:139px">
      <svg width="16" height="16" viewBox="0 0 16 16"><rect y="6.5" width="16" height="3" fill="#fff"/><rect x="6.5" width="3" height="16" fill="#fff"/></svg>
    </div>
  </article>

  <h2 class="section-title" style="top:2878px">Meeting Point</h2>
  <div class="map" role="img" aria-label="Map of Grand Cayman island">
    <div class="addr">
      <svg width="36" height="40" viewBox="0 0 36 40" fill="none" stroke="var(--blue)" stroke-width="2"><path d="M18 30s9-8 9-15a9 9 0 0 0-18 0c0 7 9 15 9 15z" stroke="var(--green)"/><circle cx="18" cy="15" r="3.5" stroke="var(--green)"/><path d="M8 28l-6 10h32l-6-10"/></svg>
      <h6>Address:</h6>
      <p>100- Lorem ipsum is simply dummy text, Cayman Islands.</p>
      <a class="btn">Get Directions</a>
    </div>
  </div>

  <h2 class="section-title" style="top:3410px">Gallery</h2>
  <div class="arrow" style="left:80px"><svg width="12" height="16" viewBox="0 0 12 16" fill="none" stroke="#fff" stroke-width="2.5"><path d="M9 2L3 8l6 6"/></svg></div>
  <div class="shot" role="img" aria-label="Photo of a lit underground cave with stalactites and a pool" style="left:169px;background:linear-gradient(160deg,#5a4a34,#b09060 45%,#2f6a6a)"></div>
  <div class="shot" role="img" aria-label="Photo of a swimmer with a dolphin in blue water" style="left:486px;background:linear-gradient(180deg,#6fb3e8,#1d7fcc 60%,#0f5ea8)"></div>
  <div class="shot" role="img" aria-label="Photo of a horse swimming in the sea with a rider" style="left:801px;background:linear-gradient(160deg,#7fc3e0,#3a8fb8 55%,#8a5a3a)"></div>
  <div class="arrow" style="left:1146px"><svg width="12" height="16" viewBox="0 0 12 16" fill="none" stroke="#fff" stroke-width="2.5"><path d="M3 2l6 6-6 6"/></svg></div>
</main>

<section class="planner">
  <div class="dots"><i></i><i class="on"></i><i></i><i></i></div>
  <h4>Use Our Online Trael Planner</h4>
  <p>Lorem Ipsum is simply dummy text of the printing and typesetting industry. Lorem Ipsum has been the industry's standard dummy text ever since the 1500s, when an unknown printer took a galley of type and scrambled it to make a type specimen book. It has survived not only five centuries, but also the leap into electronic typesetting, remaining essentially unchanged.</p>
  <a class="btn b1">Go to trip Planner</a>
  <a class="btn btn-outline b2">View Video</a>
  <div class="illus" role="img" aria-label="Illustration of a traveller planning a trip on a laptop with luggage">
    <div class="play"></div>
  </div>
</section>

<footer class="footer">
  <div class="brand"><i></i>IsleRoute</div>
  <p class="about">Lorem Ipsum is simply dummy text of the printing and typesetting industry. Lorem Ipsum has been the industry's standard dummy text ever since the 1500s.</p>
  <div class="social"><i></i><i></i><i class="fill"></i><i class="fill"></i></div>

  <h5 style="left:408px">Menu</h5>
  <ul style="left:408px"><li>Discover Cayman</li><li>Thing to do</li><li>My Trip Planner</li><li>Map</li><li>Contact Us</li></ul>

  <h5 style="left:644px">Sitemap</h5>
  <ul style="left:644px"><li>Activity description</li><li>Gallery</li><li>Meeting</li><li>Review</li><li>Locations</li><li>Languages Spoken</li></ul>

  <h5 style="left:880px">Contact info</h5>
  <div class="contact">
    <div><svg width="20" height="20" viewBox="0 0 20 20" fill="none" stroke="var(--blue)" stroke-width="2"><path d="M4 2h4l2 5-2.5 1.5a11 11 0 0 0 4 4L13 10l5 2v4a2 2 0 0 1-2 2A16 16 0 0 1 2 4a2 2 0 0 1 2-2z"/></svg><span>+91-000-000-0000</span></div>
    <div><svg width="20" height="16" viewBox="0 0 20 16" fill="none" stroke="var(--blue)" stroke-width="2"><rect x="1" y="1" width="18" height="14"/><path d="M1 1l9 8 9-8"/></svg><span>hello@isleroute.net</span></div>
    <div><svg width="20" height="22" viewBox="0 0 20 22" fill="none" stroke="var(--blue)" stroke-width="2"><path d="M10 20s7-7 7-12a7 7 0 0 0-14 0c0 5 7 12 7 12z"/><circle cx="10" cy="8" r="2.5"/></svg><span>100- lorem ipsum is simply<br>dummy text.</span></div>
  </div>
</footer>
<div class="copy">Copyright 2019. IsleRoute. Terms &amp; Conditions | Privacy Policy</div>

</body>
</html>
```